I need a business card.

I need a simple, minimalist, business card. I think the coolest business card I have ever seen is Marty Vexler's from Kestrel's 9... it is just a little creepy for the real world.
I am a photographer and I need a card that I can give to brides or potential portrait customers that is simple and classy.
My name is Glen Hardesty. My website is www.glenhardesty-example.com
Please design my card.
I think it could be as simple as my name, phone # and website... where the rest of my contact could be found... or maybe my email and no website... I am open to ideas. I imagined the card on thick card stock with a black background...

```html
<!DOCTYPE html>
<html lang="en">
<head>
<meta charset="utf-8">
<title>Glen Hardesty – Business Card</title>
<link rel="stylesheet" href="https://fonts.googleapis.com/css2?family=Crimson+Text:wght@400;700&family=Arimo:wght@400;700&family=PT+Sans&display=swap">
<style>
  :root {
    --ink: #0a0a0b;
    --paper: #ffffff;
    --card-black: #08090b;
    --label: #000000;
  }
  * { margin: 0; padding: 0; box-sizing: border-box; }
  html, body {
    width: 1200px;
    height: 2833px;
    overflow: hidden;
    background: var(--paper);
  }
  .sheet {
    position: relative;
    width: 1200px;
    height: 2833px;
  }
  .card {
    position: absolute;
    left: 0;
    width: 1200px;
    height: 1200px;
  }
  .card--front {
    top: 0;
    background: var(--card-black);
  }
  .card--back {
    top: 1500px;
    background: var(--paper);
    border: 2px solid var(--ink);
  }
  .abs { position: absolute; line-height: 1; white-space: nowrap; }

  .front-name {
    left: 134px;
    top: 468px;
    font-family: "Crimson Text", serif;
    font-weight: 400;
    font-size: 114px;
    color: var(--paper);
  }
  .front-rule {
    left: 627px;
    top: 614px;
    width: 3px;
    height: 96px;
    background: var(--paper);
  }
  .front-role {
    left: 656px;
    top: 618px;
    font-family: "Crimson Text", serif;
    font-size: 62px;
    color: var(--paper);
  }

  .back-name {
    right: 134px;
    top: 2364px;
    font-family: "Crimson Text", serif;
    font-weight: 700;
    font-size: 62px;
    color: var(--ink);
  }
  .back-rule {
    left: 1094px;
    top: 2340px;
    width: 3px;
    height: 84px;
    background: var(--ink);
  }
  .contact {
    right: 104px;
    font-size: 46px;
    color: var(--ink);
  }
  .contact--web { top: 2484px; }
  .contact--tel { top: 2566px; }
  .contact-label {
    font-family: "Arimo", sans-serif;
    font-weight: 700;
    color: var(--label);
    margin-right: 20px;
  }
  .contact-value {
    font-family: "Arimo", sans-serif;
    font-weight: 400;
    letter-spacing: 1px;
    color: #222;
  }
  .contact--tel .contact-value { letter-spacing: 7px; }

  .caption {
    font-family: "PT Sans", sans-serif;
    font-size: 78px;
    color: var(--ink);
  }
  .caption--front { left: 64px; top: 1270px; }
  .caption--back { left: 322px; top: 2758px; }
</style>
</head>
<body>
<main class="sheet">
  <section class="card card--front" aria-label="Card front">
    <div class="abs front-name">Glen Hardesty</div>
    <div class="abs front-rule"></div>
    <div class="abs front-role">photographer</div>
  </section>
  <p class="abs caption caption--front">one side card</p>

  <section class="card card--back" aria-label="Card back"></section>
  <div class="abs back-name">Glen Hardesty</div>
  <div class="abs back-rule"></div>
  <div class="abs contact contact--web"><span class="contact-label">Web:</span><span class="contact-value">www.glenhardesty-example.com</span></div>
  <div class="abs contact contact--tel"><span class="contact-label">Tel:</span><span class="contact-value">555.014.2287</span></div>
  <p class="abs caption caption--back">other side card</p>
</main>
</body>
</html>
```